GRA Stationary
GRA, Garnet Resale Advisors
Professional
Dominic T. Harlow
P.O. box 382
Marlow Ridge, Md 19507
dtharlow@graadvllc.com
graadvllc.com
I'm open to all ideas. GRA specializes in estate or antique jewelry. So a period approach(Victorian, deco, etc.) might work. But I also like a clean, modern look as well. Color scheme will probably revolve around platinum, but again, I'm open to ideas. Thanks!
needs to have business card, letterhead, fax, and envelope design
logo vector file
KX Press business card format
RGB Color Chart
GRA logo

```html
<!DOCTYPE html>
<html lang="en">
<head>
<meta charset="utf-8">
<title>GRA Stationary – Business Card</title>
<link href="https://fonts.googleapis.com/css2?family=Open+Sans:wght@400;600;700&display=swap" rel="stylesheet">
<style>
  :root {
    --bg: #e4e4e6;
    --card: #ffffff;
    --card-edge: #d6d6d8;
    --ink: #1c1c1c;
    --ink-soft: #555555;
    --rule: #9a9a9a;
    --band-dark: #141414;
    --band-grey: #8a8a8a;
    --icon-fg: #ffffff;
  }
  * { box-sizing: border-box; margin: 0; padding: 0; }
  html, body {
    width: 1200px; height: 864px; overflow: hidden;
    background: var(--bg);
    font-family: "Open Sans", Arial, sans-serif;
    color: var(--ink);
  }
  .stage {
    position: relative; width: 1200px; height: 864px;
    display: flex; align-items: center; justify-content: center; gap: 60px;
  }
  .card {
    position: relative; width: 520px; height: 300px;
    background: var(--card);
    border-radius: 22px;
    box-shadow: 0 2px 0 var(--card-edge), 0 14px 30px rgba(0,0,0,.12);
    overflow: hidden;
  }
  .brand { display: flex; flex-direction: column; align-items: center; gap: 8px; }
  .brand-mark {
    display: flex; align-items: center; gap: 10px;
    font-weight: 600; font-size: 34px; letter-spacing: 4px; color: var(--ink);
  }
  .brand-mark .dot { width: 12px; height: 12px; border-radius: 50%; background: var(--ink); }
  .brand-name { font-weight: 600; font-size: 15px; letter-spacing: 1px; color: var(--ink); }

  .card--front { display: flex; align-items: center; justify-content: center; }
  .card--front .brand { transform: translateY(-6px); }

  .card--back .brand { position: absolute; left: 40px; top: 38px; align-items: flex-start; }
  .card--back .brand-mark { font-size: 26px; letter-spacing: 3px; }
  .card--back .brand-name { font-size: 12px; }

  .contact { position: absolute; left: 40px; top: 148px; display: flex; gap: 18px; }
  .person { width: 150px; text-align: right; }
  .person-name { font-weight: 700; font-size: 13px; }
  .person-title { font-size: 10px; color: var(--ink-soft); margin-bottom: 14px; }
  .person-address { font-size: 10px; line-height: 1.5; color: var(--ink-soft); }
  .divider { width: 1px; background: var(--rule); }
  .lines { list-style: none; font-size: 10px; line-height: 1; color: var(--ink-soft); }
  .lines li { display: flex; align-items: center; gap: 7px; height: 18px; white-space: nowrap; }
  .icon {
    width: 13px; height: 13px; border-radius: 50%; background: var(--ink-soft);
    display: flex; align-items: center; justify-content: center; flex: none;
  }
  .icon svg { width: 8px; height: 8px; }
  .swoosh { position: absolute; right: 0; top: 0; width: 110px; height: 300px; }
</style>
</head>
<body>
<main class="stage">
  <section class="card card--front">
    <div class="brand">
      <div class="brand-mark"><span class="dot"></span>GRA</div>
      <div class="brand-name">Garnet Resale Advisors</div>
    </div>
  </section>

  <section class="card card--back">
    <div class="brand">
      <div class="brand-mark"><span class="dot"></span>GRA</div>
      <div class="brand-name">Garnet Resale Advisors</div>
    </div>

    <div class="contact">
      <div class="person">
        <div class="person-name">Dominic T. Harlow</div>
        <div class="person-title">President</div>
        <div class="person-address">P.O. box 382 Marlow<br>Ridge, Md 19507</div>
      </div>
      <div class="divider"></div>
      <ul class="lines">
        <li><span class="icon"><svg viewBox="0 0 10 10"><path d="M2 1h2l1 2-1 1q1 2 2 2l1-1 2 1v2q-1 1-2 1Q1 9 1 2q0-1 1-1z" fill="var(--icon-fg)"/></svg></span>(555) 318-4706</li>
        <li><span class="icon"><svg viewBox="0 0 10 10"><rect x="2" y="1" width="6" height="3" fill="var(--icon-fg)"/><rect x="1" y="4" width="8" height="4" fill="var(--icon-fg)"/></svg></span>(555) 264-9031</li>
        <li><span class="icon"><svg viewBox="0 0 10 10"><rect x="3" y="1" width="4" height="8" rx="1" fill="var(--icon-fg)"/></svg></span>(555) 471-5583</li>
        <li><span class="icon"><svg viewBox="0 0 10 10"><rect x="1" y="2.5" width="8" height="5" fill="var(--icon-fg)"/><path d="M1 2.5l4 3 4-3" stroke="#555555" stroke-width=".8" fill="none"/></svg></span>dtharlow@graadvllc.com</li>
        <li><span class="icon"><svg viewBox="0 0 10 10"><circle cx="5" cy="5" r="3.5" stroke="var(--icon-fg)" fill="none"/><path d="M1.5 5h7M5 1.5v7" stroke="var(--icon-fg)" stroke-width=".8"/></svg></span>www.graadvllc.com</li>
      </ul>
    </div>

    <svg class="swoosh" viewBox="0 0 110 300" preserveAspectRatio="none" aria-hidden="true">
      <path d="M110 0 L80 0 C40 70 40 120 70 170 C95 215 70 265 40 300 L110 300 Z" fill="var(--band-grey)"/>
      <path d="M110 0 L92 0 C55 70 55 120 82 170 C106 215 84 265 56 300 L110 300 Z" fill="var(--card)"/>
      <path d="M110 0 L98 0 C62 70 62 120 88 170 C112 215 92 265 64 300 L110 300 Z" fill="var(--band-dark)"/>
    </svg>
  </section>
</main>
</body>
</html>
```